Website for Wedding Cake Business based in Suffolk countryside

I need a website to advertise my services. I bake wedding cakes and celebration cakes. My style of baking is very rustic and I use lots of local and homegrown ingredients within my baking. I’d like the website to be classy but countryside chic. I want to website to reflect quality and sophistication but also keep the countryside vibe. My logo is currently a mustard yellow and grey but this may be changed so the colour palette is completely open.

Target Market(s)

Couples and women aged 21-40

Industry/Entity Type

Wedding

Number of Pages Required

4 page

Colors

Designer to choose colors to be used in the design.

Requirements
Must have
• Must appeal to men and women. Must have a contact button, social media links, price list and photo gallery.
• Functioning drop downs (price list, gallery, booking form)
Nice to have
• Very simple layout with menu bar across the top of the page. A section can update which shows which feeding Faye or show I’ll be a next with a map.
Should not have
• Nothing to bold, block coloured or cheesy.

```html
<!DOCTYPE html>
<html lang="en">
<head>
<meta charset="utf-8">
<title>Hazelbrook – Coffee and Bakehouse</title>
<link href="https://fonts.googleapis.com/css2?family=Lobster&family=Open+Sans:wght@400;600;700&display=swap" rel="stylesheet">
<style>
:root{
  --ink:#4a2a2e;
  --body:#5a4a4c;
  --yellow:#f3e36a;
  --blush:#fadcd4;
  --blush-btn:#fde0da;
  --mint:#d8ecdf;
  --nav:#e3ebf3;
  --line:#ececec;
  --white:#ffffff;
  --muted:#8a8a8a;
  --photo-a:#eef4f2;
  --photo-b:#d3e6e1;
}
*{margin:0;padding:0;box-sizing:border-box}
html,body{width:1200px;height:2375px;overflow:hidden;background:var(--white)}
body{font-family:"Open Sans",Arial,sans-serif;color:var(--body);position:relative}
.script{font-family:"Lobster",cursive;font-weight:400}
.abs{position:absolute}

.promo-bar{top:0;left:0;width:1200px;height:26px;background:#fafafa;border-top:3px solid var(--blush);font-size:9px;letter-spacing:1px;text-align:center;line-height:23px;color:#555}
.promo-bar b{color:#333}
.promo-close{right:150px;top:3px;font-size:13px;line-height:23px;color:#555}

.brand{top:36px;left:551px;width:98px;height:70px;border:2px solid var(--yellow);text-align:center}
.brand-mark{display:block;width:14px;height:14px;background:var(--yellow);margin:8px auto 4px}
.brand-name{font-size:14px;font-weight:600;color:var(--body);letter-spacing:.5px;line-height:18px}
.brand-sub{top:108px;left:551px;width:98px;text-align:center;font-size:6px;color:#333}

.main-nav{top:127px;left:0;width:1200px;height:36px;background:var(--nav);display:flex;justify-content:center;gap:56px;align-items:center}
.main-nav a{font-size:11px;letter-spacing:1.5px;color:#333;text-decoration:none}

.hero{top:163px;left:0;width:1200px;height:432px;background:radial-gradient(circle at 30% 40%,#d8c7a8,#8a6647 55%,#5a3d2c)}
.hero-arrow{top:342px;width:20px;height:30px}
.hero-title{top:248px;left:0;width:1200px;text-align:center;color:var(--white);font-weight:400}
.hero-title .small{font-size:34px;display:block;letter-spacing:2px}
.hero-title .big{font-size:88px;display:block;line-height:92px}
.hero-divider{top:385px;left:530px}
.btn-book{top:454px;left:510px;width:182px;height:40px;border-radius:20px;background:var(--blush-btn);color:var(--ink);font-weight:700;font-size:17px;text-align:center;line-height:40px}

.intro-title{top:660px;left:234px;width:358px;text-align:center;font-weight:400}
.intro-title .l1{display:block;font-size:38px;color:var(--yellow);line-height:44px}
.intro-title .l2{display:block;font-size:38px;color:var(--ink);line-height:44px}
.divider{display:block;margin:10px auto 0}
.intro-copy{top:795px;left:234px;width:358px;font-size:10px;line-height:15.2px;text-align:justify;color:var(--body)}
.intro-copy p{margin-bottom:14px}
.btn-order{top:972px;left:341px;width:144px;height:40px;background:var(--mint);color:var(--ink);font-weight:700;font-size:13px;letter-spacing:1px;text-align:center;line-height:40px}
.intro-photo{top:657px;left:641px;width:274px;height:360px;background:linear-gradient(var(--photo-a),var(--photo-b))}

.cakes{top:1081px;left:0;width:1200px;height:475px;background:var(--blush)}
.section-title{left:0;width:1200px;text-align:center;font-size:42px;color:var(--ink)}
.cake-card{top:1236px;width:163px;height:263px;border:1px solid #e3c8c1}

.event-card{top:1703px;width:235px}
.event-photo{height:132px;border-radius:4px}
.event-meta{display:flex;margin-top:20px;gap:19px}
.event-date{width:42px;height:43px;background:var(--mint);text-align:center;color:var(--ink);flex-shrink:0}
.event-date .d{display:block;font-size:18px;font-weight:600;line-height:24px}
.event-date .m{display:block;font-size:12px;line-height:14px}
.event-title{font-size:20px;font-weight:600;color:var(--ink);line-height:24px;white-space:nowrap}
.event-text{font-size:9.5px;line-height:15px;color:var(--body);margin-top:4px}
.dot{top:1966px;width:10px;height:10px;border-radius:50%}

.footer{top:2031px;left:0;width:1200px;height:260px;border-top:1px solid var(--line)}
.foot-brand{top:2074px;left:234px;width:100px;height:66px;border:2px solid var(--yellow);text-align:center}
.foot-sub{top:2145px;left:234px;width:100px;text-align:center;font-size:6px;color:#333}
.foot-col{top:2074px}
.foot-col h4{font-size:10.5px;font-weight:700;letter-spacing:.5px;color:#222;margin-bottom:10px}
.foot-col li{list-style:none;font-size:9.5px;line-height:15.2px;color:#333}
.social{display:flex;gap:20px;margin-top:22px}
.social span{width:12px;height:12px;border-radius:50%;background:#333}
.copyright{top:2291px;left:0;width:1200px;height:84px;border-top:1px solid var(--line);text-align:center;font-size:9px;line-height:64px;color:var(--muted)}
</style>
</head>
<body>

<div class="abs promo-bar">FREE DELIVERY ON ORDERS OVER $50. <b>SHOP NOW</b></div>
<div class="abs promo-close">×</div>

<div class="abs brand"><span class="brand-mark"></span><div class="brand-name">HAZELBROOK</div></div>
<div class="abs brand-sub">Coffee and Bakehouse</div>

<nav class="abs main-nav"><a>HOME</a><a>INFORMATION</a><a>GALLERY</a><a>CONTACT US</a></nav>

<section class="abs hero" role="img" aria-label="Overhead photo of frosted cupcakes topped with edible flowers on a cooling rack"></section>
<svg class="abs hero-arrow" style="left:28px" viewBox="0 0 20 30"><path d="M14 4 L5 15 L14 26" fill="none" stroke="#fff" stroke-width="3"/></svg>
<svg class="abs hero-arrow" style="left:1148px" viewBox="0 0 20 30"><path d="M6 4 L15 15 L6 26" fill="none" stroke="#fff" stroke-width="3"/></svg>
<h1 class="abs hero-title script"><span class="small">Welcome to</span><span class="big">Hazelbrook</span></h1>
<svg class="abs hero-divider" width="140" height="20" viewBox="0 0 140 20"><path d="M4 10 H58 M82 10 H136" stroke="#fff" stroke-width="1.5"/><circle cx="70" cy="10" r="5" fill="#fff"/></svg>
<div class="abs btn-book">BOOK NOW!</div>

<h2 class="abs intro-title script"><span class="l1">Made For You</span><span class="l2">With Love</span>
<svg class="divider" width="66" height="14" viewBox="0 0 66 14"><path d="M2 7 H26 M40 7 H64" stroke="#4a2a2e" stroke-width="1.2"/><circle cx="33" cy="7" r="4" fill="none" stroke="#4a2a2e"/></svg></h2>
<div class="abs intro-copy">
<p>Lorem ipsum dolor sit amet, consectetur adipiscing elit. Vivamus eget metus aliquet, fermentum ex in, ornare quam. Donec imperdiet ut metus sed tincidunt. Aenean vestibulum semper nibh non ullamcorper. Morbi ornare est eros, non fringilla elit lacinia in. Nullam molestie augue in dolor gravida molestie. Donec egestas ipsum vel nisi aliquam, non eleifend purus semper. Nullam sed finibus sem. Nulla nec ligula consequat, pulvinar nisi at, condimentum eros.</p>
<p>Etiam id quam sollicitudin, convallis nisi sit amet, varius lorem. Morbi id quam risus. Morbi ligula felis, aliquam quis commodo vitae, vestibulum ac nisi. Nullam ac porta neque.</p>
</div>
<div class="abs btn-order">ORDER NOW!</div>
<div class="abs intro-photo" role="img" aria-label="Photo of a three-tier wedding cake on a cake stand"></div>

<section class="abs cakes"></section>
<h2 class="abs section-title script" style="top:1112px">Choose Your Cake</h2>
<svg class="abs" style="top:1175px;left:567px" width="66" height="14" viewBox="0 0 66 14"><path d="M2 7 H26 M40 7 H64" stroke="#4a2a2e" stroke-width="1.2"/><circle cx="33" cy="7" r="4" fill="none" stroke="#4a2a2e"/></svg>
<div class="abs cake-card" style="left:226px;background:linear-gradient(#cfe3dc,#f4f1ec)" role="img" aria-label="White tiered cake with cascading peach roses"></div>
<div class="abs cake-card" style="left:408px;background:linear-gradient(#8a6a4e,#d8b8b0)" role="img" aria-label="Semi-naked tiered cake with pink flowers"></div>
<div class="abs cake-card" style="left:590px;background:linear-gradient(#5a4a48,#ece6e2)" role="img" aria-label="White ruffled tiered cake"></div>
<div class="abs cake-card" style="left:772px;background:linear-gradient(#eae4de,#d9a06a)" role="img" aria-label="Naked sponge cake with strawberries and berries"></div>

<h2 class="abs section-title script" style="top:1598px">Upcoming Events</h2>
<svg class="abs" style="top:1661px;left:567px" width="66" height="14" viewBox="0 0 66 14"><path d="M2 7 H26 M40 7 H64" stroke="#4a2a2e" stroke-width="1.2"/><circle cx="33" cy="7" r="4" fill="none" stroke="#4a2a2e"/></svg>

<article class="abs event-card" style="left:234px">
<div class="event-photo" style="background:linear-gradient(#c9b6a6,#f2ede8)" role="img" aria-label="White cake decorated with purple sugar roses"></div>
<div class="event-meta"><div class="event-date"><span class="d">30</span><span class="m">April</span></div>
<div><div class="event-title">Wedding Party</div><p class="event-text">Lorem ipsum dolor sit amet, consectetur adipiscing elit. Vivamus eget metus aliquet, fermentum ex in, ornare quam.</p></div></div>
</article>
<article class="abs event-card" style="left:484px">
<div class="event-photo" style="background:linear-gradient(#f4c7d3,#d98aa4)" role="img" aria-label="Pink celebration cake with red and white piping"></div>
<div class="event-meta"><div class="event-date"><span class="d">30</span><span class="m">April</span></div>
<div><div class="event-title">Celebration Party</div><p class="event-text">Lorem ipsum dolor sit amet, consectetur adipiscing elit. Vivamus eget metus aliquet, fermentum ex in, ornare quam.</p></div></div>
</article>
<article class="abs event-card" style="left:733px">
<div class="event-photo" style="background:linear-gradient(#e4e2e2,#f0b8c8)" role="img" aria-label="Rainbow layer birthday cake with candles and sprinkles"></div>
<div class="event-meta"><div class="event-date"><span class="d">30</span><span class="m">April</span></div>
<div><div class="event-title">Wedding Party</div><p class="event-text">Lorem ipsum dolor sit amet, consectetur adipiscing elit. Vivamus eget metus aliquet, fermentum ex in, ornare quam.</p></div></div>
</article>
<span class="abs dot" style="left:575px;background:#f7cfc6"></span>
<span class="abs dot" style="left:591px;background:var(--mint)"></span>
<span class="abs dot" style="left:607px;background:var(--mint)"></span>

<footer class="abs footer"></footer>
<div class="abs foot-brand"><span class="brand-mark"></span><div class="brand-name">HAZELBROOK</div></div>
<div class="abs foot-sub">Coffee and Bakehouse</div>
<div class="abs foot-col" style="left:381px"><h4>CATEGORIES</h4><ul>
<li>Edibles</li><li>Tools</li><li>Weeding Cake</li><li>Birthday Cake</li><li>Party Cake</li><li>Anniversary Cake</li><li>Decorations</li><li>Colours</li><li>Boards &amp; Boxes</li><li>Sale</li></ul></div>
<div class="abs foot-col" style="left:548px"><h4>USEFUL LINKS</h4><ul>
<li>About us</li><li>Cake Gallery</li><li>Our Brands</li><li>Delivery</li><li>Support</li><li>Contact Us</li></ul></div>
<div class="abs foot-col" style="left:734px"><h4>CONTACT US</h4><ul>
<li>hazelbrook</li><li>134 Lorem Ipsum Dolor Sit,</li><li>ndw, 2564</li><li>Country</li><li>&nbsp;</li><li>+610 123 456 7890</li></ul>
<div class="social"><span></span><span></span><span></span><span></span></div></div>
<div class="abs copyright">© 2019 Hazelbrook. All rights reserved.</div>

</body>
</html>
```